Sleep Consulting Business

Hello I need a business card design with similar colors to my logo that was created. I help mom/parents whose little ones are having sleep issues. Are you able to recreate the picture with the girl sleeping onto a business card using a picture that I provide. That would be one side with my logo on top and on the other side would the following:
My name (in bigger letters than the rest. maybe written in script
title
email
website
phone
instagram
I have included color Inspo
Contact Information for Business Card
Full Name, number, email, website, ig page
Look and feel
Each slider illustrates characteristics of the customer's brand and the style your logo design should communicate.

```html
<!DOCTYPE html>
<html lang="en">
<head>
<meta charset="UTF-8">
<title>Snug Till Dawn – Business Card</title>
<link href="https://fonts.googleapis.com/css2?family=Montserrat:wght@400;500&family=Allura&display=swap" rel="stylesheet">
<style>
  :root {
    --backdrop: #8a6d52;
    --card-white: #ffffff;
    --card-blush: #cfae9c;
    --rose-copper: #c98f78;
    --copper-deep: #a9735a;
    --taupe: #8f8079;
    --ink: #2f2a28;
    --mist: #eeedf0;
    --hair: #8e6a55;
    --skin: #d9a994;
    --blanket: #e3cfb6;
  }
  * { margin: 0; padding: 0; box-sizing: border-box; }
  html, body { width: 900px; height: 1200px; overflow: hidden; }
  body {
    background: var(--backdrop);
    font-family: "Montserrat", Arial, sans-serif;
    position: relative;
  }
  .card {
    position: absolute;
    left: 80px;
    width: 742px;
    height: 440px;
    border-radius: 32px;
    overflow: hidden;
    box-shadow: 0 4px 10px rgba(0,0,0,0.45);
  }
  .card--front { top: 132px; background: var(--card-white); }
  .card--back { top: 638px; background: var(--card-blush); }

  .front-accent {
    position: absolute;
    left: 410px;
    top: 160px;
    width: 230px;
    height: 230px;
    border-radius: 50%;
    background: var(--mist);
    opacity: 0.8;
  }
  .brand-name {
    position: absolute;
    left: 34px;
    top: 74px;
    font-weight: 500;
    font-size: 31px;
    letter-spacing: 3px;
    color: var(--taupe);
    text-transform: uppercase;
    white-space: nowrap;
  }

  .person-name {
    position: absolute;
    left: 44px;
    top: 226px;
    font-family: "Allura", cursive;
    font-size: 46px;
    line-height: 1;
    color: var(--rose-copper);
  }
  .person-title {
    position: absolute;
    left: 46px;
    top: 280px;
    font-size: 16px;
    color: var(--ink);
  }
  .contact-list {
    position: absolute;
    left: 46px;
    top: 319px;
    list-style: none;
  }
  .contact-list li {
    display: flex;
    align-items: center;
    height: 22.5px;
    font-size: 15.5px;
    color: var(--ink);
  }
  .contact-list svg {
    width: 14px;
    height: 14px;
    margin-right: 11px;
    flex: none;
    fill: var(--rose-copper);
  }

  .back-photo {
    position: absolute;
    left: 30px;
    top: 40px;
    width: 700px;
    height: 400px;
    background:
      radial-gradient(ellipse 130px 110px at 150px 120px, rgba(142,106,85,0.75), rgba(142,106,85,0) 100%),
      radial-gradient(ellipse 170px 120px at 210px 200px, rgba(217,169,148,0.9), rgba(217,169,148,0) 100%),
      radial-gradient(ellipse 240px 80px at 200px 310px, rgba(214,164,142,0.85), rgba(214,164,142,0) 100%),
      radial-gradient(ellipse 230px 150px at 480px 190px, rgba(227,207,182,0.85), rgba(227,207,182,0) 100%);
  }
  .back-brand {
    position: absolute;
    left: 0;
    right: 0;
    top: 196px;
    text-align: center;
    font-weight: 500;
    font-size: 46px;
    letter-spacing: 4px;
    color: var(--copper-deep);
    text-transform: uppercase;
  }
</style>
</head>
<body>

  <section class="card card--front">
    <div class="front-accent" aria-hidden="true"></div>
    <div class="brand-name">Snug Till Dawn</div>

    <div class="person-name">Daniel Brooks</div>
    <div class="person-title">CEO &amp; Founder</div>

    <ul class="contact-list">
      <li>
        <svg viewBox="0 0 16 16" aria-hidden="true"><path d="M3 2h3l1 3-2 1c1 2 2 3 4 4l1-2 3 1v3c0 1-1 2-2 2C6 14 2 10 2 4c0-1 0-2 1-2z"/></svg>
        215-555-0147
      </li>
      <li>
        <svg viewBox="0 0 16 16" aria-hidden="true"><path d="M1 3h14v1.5L8 9 1 4.5zM1 6l7 4.5L15 6v7H1z"/></svg>
        hello@snugtilldawn.com
      </li>
      <li>
        <svg viewBox="0 0 16 16" aria-hidden="true"><circle cx="8" cy="8" r="6.5" fill="none" stroke="#c98f78" stroke-width="1.6"/><path d="M1.5 8h13M8 1.5c-3 3-3 10 0 13M8 1.5c3 3 3 10 0 13" fill="none" stroke="#c98f78" stroke-width="1.2"/></svg>
        www.snugtilldawn.com
      </li>
      <li>
        <svg viewBox="0 0 16 16" aria-hidden="true"><circle cx="8" cy="8" r="6.5"/></svg>
        @snugtilldawnsleep
      </li>
    </ul>
  </section>

  <section class="card card--back">
    <div class="back-photo" role="img" aria-label="Soft-toned photo of a newborn sleeping on folded arms, wrapped in a knit blanket"></div>
    <div class="back-brand">Snug Till Dawn</div>
  </section>

</body>
</html>
```